Pitch deck for fundraising for a timber drying business

We have the basic content in a powerpoint but need someone to take that and make an attractive and engaging document for a reader who may see hundreds of these a week so visual impact is key.
We are launching a timber drying business in Australia using an exclusive line of kilns not otherwise available in Australia.
Designs should focus on natural tones and connections with forests and timber, probably with a green (colour) focus.
Updates

Sick

Target Market(s)

investors, wealthyindividuals

Colors

Designer to choose colors to be used in the design.

Requirements
Nice to have
• Design in Canva or similar

```html
<!DOCTYPE html>
<html lang="en">
<head>
<meta charset="utf-8">
<title>Redgum Kilns – Pitch Deck</title>
<link rel="stylesheet" href="https://fonts.googleapis.com/css2?family=Montserrat:wght@300;400;600;700;800&display=swap">
<style>
  :root {
    --page: #e8eae6;
    --white: #ffffff;
    --brand-green: #5cb947;
    --chevron-dark: #3aa84a;
    --chevron-light: #8cc63f;
    --tag-green: #6cc04a;
    --tag-light: #9fd25a;
    --ink: #222222;
    --forest-dark: #161d12;
    --forest-mid: #2c3a1f;
    --forest-light: #7fa43a;
    --log-dark: #6b4a2c;
    --log-light: #c79a66;
    --shadow: 0 6px 14px rgba(0,0,0,.18);
  }
  * { box-sizing: border-box; margin: 0; padding: 0; }
  html, body { width: 829px; height: 1200px; overflow: hidden; }
  body {
    background: var(--page);
    font-family: "Montserrat", Arial, sans-serif;
    color: var(--ink);
    position: relative;
  }
  .slide {
    position: absolute;
    background: var(--white);
    box-shadow: var(--shadow);
    overflow: hidden;
  }
  .slide-art { position: absolute; inset: 0; width: 100%; height: 100%; }

  /* Title slide */
  .slide--title { left: 108px; top: 80px; width: 612px; height: 340px; }
  .title-block { position: absolute; left: 315px; top: 100px; }
  .title-block__name {
    font-weight: 800; font-size: 45px; line-height: 46px;
    color: var(--brand-green); text-transform: uppercase; letter-spacing: .5px;
  }
  .title-block__sub {
    font-weight: 400; font-size: 32px; line-height: 38px; margin-top: 2px;
    letter-spacing: .5px;
  }

  /* Text slides (introduction, market overview) */
  .slide--intro { left: 34px; top: 470px; width: 375px; height: 212px; }
  .slide--market { left: 108px; top: 732px; width: 612px; height: 340px; }
  .brand-mark {
    position: absolute; font-weight: 800; color: var(--brand-green);
    text-transform: uppercase; line-height: 1.05;
  }
  .slide--intro .brand-mark { left: 262px; top: 19px; font-size: 13.5px; }
  .slide--market .brand-mark { left: 436px; top: 36px; font-size: 22px; }
  .copy { position: absolute; color: var(--white); }
  .copy__heading { font-weight: 800; text-transform: uppercase; letter-spacing: .2px; }
  .copy p { font-weight: 400; text-align: justify; }
  .slide--intro .copy { left: 15px; top: 22px; width: 214px; }
  .slide--intro .copy__heading { font-size: 10.5px; margin-bottom: 6px; }
  .slide--intro .copy p { font-size: 4.3px; line-height: 5.2px; margin-bottom: 5px; }
  .slide--market .copy { left: 22px; top: 44px; width: 356px; }
  .slide--market .copy__heading { font-size: 16px; margin-bottom: 10px; }
  .slide--market .copy p { font-size: 6.9px; line-height: 8.2px; margin-bottom: 8px; }

  /* Process slide */
  .slide--process { left: 425px; top: 470px; width: 375px; height: 212px; }
  .step { position: absolute; left: 18px; display: flex; align-items: flex-start; }
  .step__thumb { width: 46px; height: 40px; flex: none; }
  .step__thumb--plank { width: 46px; height: 18px; margin-top: 8px; }
  .step__body { margin-left: 6px; margin-top: 6px; }
  .step__label { font-size: 5.2px; line-height: 6.4px; font-weight: 600; width: 60px; }
  .tag {
    display: inline-block; margin-top: 3px; padding: 1px 14px 1px 4px;
    background: var(--tag-green); color: var(--white);
    font-size: 6px; font-weight: 600;
    clip-path: polygon(0 0, 100% 0, 92% 100%, 0 100%);
  }
  .tag sup { font-size: 4px; }
  .net-profit {
    position: absolute; left: 175px; top: 191px; height: 15px; display: flex;
    font-size: 8px; color: var(--white); font-weight: 500;
  }
  .net-profit__label { background: var(--tag-green); padding: 2px 8px; width: 82px; }
  .net-profit__value {
    background: var(--tag-light); padding: 2px 10px; width: 74px; font-weight: 600;
  }
  .net-profit__value sup { font-size: 5px; }
</style>
</head>
<body>

<!-- Title slide -->
<section class="slide slide--title">
  <svg class="slide-art" viewBox="0 0 612 340" preserveAspectRatio="none">
    <defs>
      <linearGradient id="forestSun" x1="0" y1="0" x2="0" y2="1">
        <stop offset="0" stop-color="#c9cfa8"/>
        <stop offset=".35" stop-color="#4d5a2c"/>
        <stop offset=".7" stop-color="#6e9a2e"/>
        <stop offset="1" stop-color="#3d5d1c"/>
      </linearGradient>
    </defs>
    <polygon points="0,0 190,0 268,170 190,340 0,340" fill="url(#forestSun)" role="img" aria-label="Photo of a sunlit pine forest with mossy ground"/>
    <polygon points="190,0 200,0 278,170 200,340 190,340 268,170" fill="var(--chevron-light)"/>
    <polygon points="236,116 254,116 300,170 254,224 236,224 282,170" fill="var(--chevron-dark)"/>
    <polygon points="252,116 266,116 312,170 266,224 252,224 298,170" fill="var(--chevron-light)" opacity=".85"/>
  </svg>
  <div class="title-block">
    <h1 class="title-block__name">Redgum<br>Kilns</h1>
    <p class="title-block__sub">PITCH DECK</p>
  </div>
</section>

<!-- Introduction slide -->
<section class="slide slide--intro">
  <svg class="slide-art" viewBox="0 0 375 212" preserveAspectRatio="none">
    <defs>
      <linearGradient id="forestDarkA" x1="0" y1="0" x2="1" y2="0">
        <stop offset="0" stop-color="var(--forest-dark)"/>
        <stop offset=".6" stop-color="var(--forest-dark)"/>
        <stop offset=".8" stop-color="var(--forest-mid)"/>
        <stop offset="1" stop-color="var(--forest-dark)"/>
      </linearGradient>
    </defs>
    <rect x="0" y="13" width="375" height="187" fill="url(#forestDarkA)" role="img" aria-label="Photo of a dark, dense forest interior"/>
    <polygon points="198,13 375,13 375,61 228,61" fill="var(--white)"/>
  </svg>
  <div class="brand-mark">Redgum<br>Kilns</div>
  <div class="copy">
    <h2 class="copy__heading">Introduction</h2>
    <p>Redgum Kilns International (RKI) has secured exclusive access to a superior timber drying technology (ArcDry kilns) that has been in commercial production since 1980.</p>
    <p>RKI will leverage this technology to build a hardwood drying business, initially focused on the stair tread market in Sydney and Brisbane.</p>
    <p>Hardwood stair tread timber has an approximate gross margin of $XXXX/m3 (XX%). RKI will sell directly to stair tread installers enabling us to retain the bulk of the gross margin as net profit.</p>
    <p>ArcDry kilns are relatively inexpensive ($US79-205K), modular in design, and return approximately 300% per annum. As a result, RKI will be able to scale without additional equity or debt funding.</p>
    <p>The Australian hardwood industry is worth around $7bn pa on 700,000m3 of sawn timber but 93% of logs are exported. With 10 kilns RKI would dry less than 1% of all sawn timber but turn over $XXm and nett $XXm with huge growth potential from value adding exported logs.</p>
    <p>This is not a tech play but a cash cow investment to be held long term. We have a simple business model, using established technology to disrupt a technologically stagnant, but growing industry.</p>
  </div>
</section>

<!-- Process / margin slide -->
<section class="slide slide--process">
  <svg class="slide-art" viewBox="0 0 375 212" preserveAspectRatio="none">
    <defs>
      <linearGradient id="logPile" x1="0" y1="0" x2="1" y2="1">
        <stop offset="0" stop-color="#8c8a62"/>
        <stop offset=".4" stop-color="var(--log-light)"/>
        <stop offset=".75" stop-color="var(--log-dark)"/>
        <stop offset="1" stop-color="#9a7148"/>
      </linearGradient>
    </defs>
    <polygon points="262,0 375,0 375,212 248,212 190,106" fill="url(#logPile)" role="img" aria-label="Photo of a stack of cut hardwood logs"/>
    <polygon points="254,0 262,0 190,106 248,212 240,212 182,106" fill="var(--chevron-light)"/>
    <polygon points="196,74 206,74 186,106 206,138 196,138 176,106" fill="var(--chevron-dark)"/>
  </svg>

  <div class="step" style="top:10px">
    <div class="step__thumb" role="img" aria-label="Photo of sawn timber boards" style="background:linear-gradient(135deg,#a7704a,#5e3a22)"></div>
    <div class="step__body"><div class="step__label">Buy cut timber<br>from sawmills</div><span class="tag">$XXX m<sup>3</sup></span></div>
  </div>
  <div class="step" style="top:62px">
    <div class="step__thumb" role="img" aria-label="Photo of timber stacked inside a drying kiln" style="background:linear-gradient(135deg,#d8c6a8,#7b5a3a)"></div>
    <div class="step__body"><div class="step__label">Buy cut timber<br>from sawmills</div><span class="tag">$XXX m<sup>3</sup></span></div>
  </div>
  <div class="step" style="top:113px">
    <div class="step__thumb" role="img" aria-label="Photo of a timber dressing machine in a workshop" style="background:linear-gradient(135deg,#9aa3ad,#4a4f55)"></div>
    <div class="step__body"><div class="step__label">Dress and<br>deliver</div><span class="tag">$XXX m<sup>3</sup></span></div>
  </div>
  <div class="step" style="top:157px">
    <div class="step__thumb step__thumb--plank" role="img" aria-label="Photo of a finished hardwood stair tread" style="background:linear-gradient(160deg,#7a4a2a,#3e2414);clip-path:polygon(0 60%,85% 0,100% 35%,15% 100%)"></div>
    <div class="step__body"><div class="step__label">Sell dried stair<br>treads to installers</div><span class="tag">$XXX m<sup>3</sup></span></div>
  </div>

  <div class="net-profit">
    <span class="net-profit__label">NET PROFIT</span>
    <span class="net-profit__value">$XXX m<sup>3</sup></span>
  </div>
</section>

<!-- Market overview slide -->
<section class="slide slide--market">
  <svg class="slide-art" viewBox="0 0 612 340" preserveAspectRatio="none">
    <defs>
      <linearGradient id="forestDarkB" x1="0" y1="0" x2="1" y2="0">
        <stop offset="0" stop-color="var(--forest-dark)"/>
        <stop offset=".62" stop-color="var(--forest-dark)"/>
        <stop offset=".78" stop-color="var(--forest-mid)"/>
        <stop offset=".9" stop-color="#4a5a2a"/>
        <stop offset="1" stop-color="var(--forest-dark)"/>
      </linearGradient>
    </defs>
    <rect x="0" y="22" width="612" height="296" fill="url(#forestDarkB)" role="img" aria-label="Photo of a dark, dense forest interior"/>
    <polygon points="325,22 612,22 612,104 402,104" fill="var(--white)"/>
  </svg>
  <div class="brand-mark">Redgum<br>Kilns</div>
  <div class="copy">
    <h2 class="copy__heading">Market Overview</h2>
    <p>The total value of the Australian timber market is $23.9bn<sup>1</sup> with hardwood accounting for over $7bn and softwood the balance. The Australian hardwood market has been growing strongly, posting 10% growth in volume of logs harvested and a 13% increase in price in 2017 despite a 5% fall in housing construction.</p>
    <p>The hardwood industry however is massively under developed with 93%<sup>2</sup> of all plantation hardwood logs being exported – with no value adding.</p>
    <p>The total volume of sawn hardwood timber in 2018 was 700,000m3. With just 10 kilns we would dry less than 6,800m3 pa, gross $30.6m in revenue and net $18.5m with significant opportunity to expand.</p>
    <p>In NSW logs are sourced through either Coastal Forests Agency (Dale knows and has worked with the Chair previously) on either a quota or spot price basis or through the logging of private forests. RKI will commence by sourcing timber from private forests as there are numerous landholders and contract loggers to ensure timber supply and mitigate sourcing risk.</p>
    <p>To quantify the direct addressable market RKI conducted extensive market research, contacting 98 stair installers, joineries and furniture manufacturers in addition to wholesalers. Stair installers pay between $XXX and $XXXXm3 with an average of just over $XX00m3 whereas wholesalers buy at around $XX00m3. Include Ross's timber data on stair tread market.</p>
  </div>
</section>

</body>
</html>
```